Ardoise Lumen Stationery design

With my provided logo I need stationery design for business cards, envelope (#10), letterhead, fax sheet, memo sheet and 9'' x 12'' presentation folder. I would aIso need an email signature design included. PMS COLORS are : Pantone 541C et 299C. Looking for a bold look, minimalist yet eye-catching look.

```html
<!DOCTYPE html>
<html lang="fr">
<head>
<meta charset="utf-8">
<title>Ardoise Lumen — Business Card</title>
<link rel="stylesheet" href="https://fonts.googleapis.com/css2?family=Lato:wght@300;400;700;900&display=swap">
<style>
  :root {
    --page-bg: #d9d6d1;
    --card-face: #ece9e4;
    --panel-deep: #0f3550;
    --panel-mid: #1f5878;
    --accent-teal: #1a8ca3;
    --name-teal: #4aa6bd;
    --panel-text: #c4d3dc;
    --brand-navy: #15344f;
  }
  * { margin: 0; padding: 0; box-sizing: border-box; }
  html, body {
    width: 1200px;
    height: 1047px;
    overflow: hidden;
    background: var(--page-bg);
    font-family: "Lato", Arial, sans-serif;
  }
  .business-card {
    position: absolute;
    left: 100px;
    top: 253px;
    width: 1000px;
    height: 540px;
    border-radius: 26px;
    overflow: hidden;
    background: var(--card-face);
    box-shadow: 0 10px 30px rgba(0, 0, 0, 0.12);
  }
  .card-shapes {
    position: absolute;
    inset: 0;
  }
  .contact-block {
    position: absolute;
    left: 58px;
    top: 82px;
    color: var(--panel-text);
  }
  .holder-name {
    font-weight: 700;
    font-size: 43px;
    letter-spacing: 0.5px;
    color: var(--name-teal);
    line-height: 1;
  }
  .holder-title {
    font-weight: 400;
    font-size: 23px;
    margin-top: 12px;
  }
  .postal-address {
    margin-top: 100px;
    font-size: 24px;
    line-height: 32px;
    font-style: normal;
  }
  .contact-list {
    list-style: none;
    margin-top: 22px;
  }
  .contact-list li {
    display: flex;
    align-items: center;
    font-size: 24px;
    height: 36px;
  }
  .contact-list svg {
    width: 26px;
    height: 26px;
    margin-right: 22px;
    flex: none;
  }
  .brand-lockup {
    position: absolute;
    left: 580px;
    width: 420px;
    top: 170px;
    display: flex;
    flex-direction: column;
    align-items: center;
  }
  .brand-square {
    width: 92px;
    height: 92px;
    border: 6px solid var(--brand-navy);
    margin-bottom: 34px;
  }
  .brand-name {
    font-weight: 700;
    font-size: 46px;
    letter-spacing: 2px;
    color: var(--brand-navy);
    white-space: nowrap;
  }
</style>
</head>
<body>
  <div class="business-card">
    <svg class="card-shapes" viewBox="0 0 1000 540" width="1000" height="540" aria-hidden="true">
      <defs>
        <linearGradient id="panelGradient" x1="0" y1="0" x2="1" y2="1">
          <stop offset="0" stop-color="var(--panel-mid)"/>
          <stop offset="1" stop-color="var(--panel-deep)"/>
        </linearGradient>
      </defs>
      <path class="blue-panel" d="M0 0 H555 C470 110 450 380 545 540 H0 Z" fill="url(#panelGradient)"/>
      <path class="teal-arc" d="M555 0 C470 110 450 380 545 540 H568 C478 380 490 120 572 0 Z" fill="var(--accent-teal)"/>
    </svg>

    <div class="contact-block">
      <h1 class="holder-name">MARC DELORME</h1>
      <p class="holder-title">Founder &amp; CEO</p>
      <address class="postal-address">
        1234 First Line Address<br>
        5678 Second Line Address
      </address>
      <ul class="contact-list">
        <li>
          <svg viewBox="0 0 24 24" fill="none" stroke="var(--accent-teal)" stroke-width="2" stroke-linecap="round" stroke-linejoin="round"><path d="M5 3h4l2 5-2.5 1.5a11 11 0 0 0 6 6L16 13l5 2v4a2 2 0 0 1-2 2A17 17 0 0 1 3 5a2 2 0 0 1 2-2z"/></svg>
          1234567890
        </li>
        <li>
          <svg viewBox="0 0 24 24" fill="none" stroke="var(--accent-teal)" stroke-width="2" stroke-linejoin="round"><rect x="2" y="5" width="20" height="14"/><path d="M2 5l10 8 10-8"/></svg>
          info@yourmail.com
        </li>
        <li>
          <svg viewBox="0 0 24 24" fill="none" stroke="var(--accent-teal)" stroke-width="2"><circle cx="12" cy="12" r="9"/><path d="M3 12h18M12 3c3 3 3 15 0 18M12 3c-3 3-3 15 0 18"/></svg>
          www.yourwebsite.com
        </li>
      </ul>
    </div>

    <div class="brand-lockup">
      <div class="brand-square"></div>
      <p class="brand-name">ARDOISE LUMEN</p>
    </div>
  </div>
</body>
</html>
```